Email Marketing Campaign 50% discount and buy-2-get-1 offer

I would like to inform my customers of our special offers via a e-Newsletter/Marketing E-Mail.

The coding needs to be done by the designer.

I have most of the design and the message that we wish to convey our buyers.

The information is:

1. We have now 50% discount on all our carpets

2. We have a buy-2 get-1 free carpet offer

For both the above messages we have already banner style that we like to use in our Newsletter.
I have attached the banner and the designers can use it.

3. We have opened a new shop in Berlin Germany

Therefore we like to have a Sylish Newsletter design that fits our website and products using the banner idea and we wish to include the 3 messages.
Special note should be given that this newsletter is going to our previous buyers. Therefore they already know us, and we just like to inform them of our latest news and offer.

Target Market(s)

Upmarket buyers looking for a great deal

Industry/Entity Type

Marketing

Coding

Coded - Design and coding required

Number of Pages Required

1 page

Font styles to use
Sans Serif

Colors
e667a6
34a7d8

Requirements
Must have
• Clear explanation with excitement in the message
Nice to have
• To promote clearly the 3 for 2 with maybe an explanation and clear images describing what the promotion is and how it works.
• I.e. buy 2 get 1 extra carpet of your choice free
• Add carpets to checkout and the system will calculate automatically
• The lowest carpet in your selection of 3 is the free carpet

```html
<!DOCTYPE html>
<html lang="en">
<head>
<meta charset="utf-8">
<title>Heirloom Rugs – Spring Newsletter</title>
<link rel="stylesheet" href="https://fonts.googleapis.com/css2?family=Montserrat:wght@400;600;700;800;900&family=Open+Sans:wght@400;600;700&family=Pacifico&display=swap">
<style>
  :root{
    --pink:#e667a6;
    --pink-deep:#d24a8c;
    --blue:#34a7d8;
    --blue-deep:#1f7fae;
    --ink:#333333;
    --grey-text:#6a6a6a;
    --grey-light:#9a9a9a;
    --panel:#eeeeee;
    --frame:#e2e2e2;
    --white:#ffffff;
    --black:#1a1a1a;
  }
  *{margin:0;padding:0;box-sizing:border-box}
  html,body{width:800px;height:1200px;overflow:hidden;background:var(--white)}
  body{position:relative;font-family:"Open Sans",Arial,sans-serif;color:var(--ink)}

  .preheader{position:absolute;top:8px;left:0;width:800px;text-align:center;font-size:10px;line-height:15px;color:var(--grey-light)}
  .preheader a{color:var(--pink);text-decoration:none}

  .newsletter{position:absolute;top:46px;left:56px;width:688px;height:1042px;border:1px solid var(--frame);background:var(--white)}

  .brand{position:absolute;top:26px;left:0;width:100%;display:flex;justify-content:center;align-items:center;gap:10px}
  .brand-dot{width:14px;height:14px;border-radius:50%;background:var(--pink)}
  .brand-name{font-family:"Montserrat",Arial,sans-serif;font-weight:700;font-size:34px;letter-spacing:1px;color:#5c5c5c}

  .hero{position:absolute;top:92px;left:19px;width:648px;height:442px;overflow:hidden;
    background:linear-gradient(160deg,#6d5a48 0%,#4a3d33 35%,#2e2a2a 70%,#3b2f36 100%)}
  .hero-photo{position:absolute;inset:0;background:radial-gradient(ellipse at 70% 20%,rgba(190,170,140,.45),transparent 60%),radial-gradient(ellipse at 40% 85%,rgba(120,60,90,.35),transparent 65%)}
  .spring-ribbon{position:absolute;top:34px;left:8px;width:250px;height:56px;transform:rotate(-9deg)}
  .spring-ribbon span{position:absolute;inset:0;display:flex;align-items:center;justify-content:center;font-family:"Pacifico",cursive;font-size:25px;color:var(--white)}

  .discount{position:absolute;top:218px;left:0;width:100%;display:flex;justify-content:center;align-items:center}
  .discount-rule{width:70px;height:8px;background:var(--white)}
  .discount-value{background:var(--black);color:var(--white);font-family:"Montserrat",Arial,sans-serif;font-weight:800;font-size:58px;line-height:78px;padding:0 24px;border-top:6px solid var(--white);border-bottom:6px solid var(--white)}

  .offer-bar{position:absolute;top:318px;left:74px;width:500px;height:46px}
  .offer-bar svg{position:absolute;inset:0}
  .offer-text{position:absolute;left:0;top:0;width:500px;height:40px;display:flex;align-items:center;justify-content:center;gap:14px;font-family:"Montserrat",Arial,sans-serif;font-weight:800;font-size:18px;color:var(--white);white-space:nowrap}
  .offer-divider{display:block;width:2px;height:24px;background:var(--white)}

  .promo{position:absolute;top:534px;left:19px;width:648px;height:404px;background:var(--panel)}
  .promo-copy{position:absolute;top:0;left:40px;width:300px;text-align:center}
  .plus{margin-top:30px;font-family:"Montserrat",Arial,sans-serif;font-weight:800;font-size:26px;color:#555}
  .ribbon{position:relative;margin:8px auto 0;width:270px;height:48px}
  .ribbon svg{position:absolute;inset:0}
  .ribbon span{position:absolute;inset:0;display:flex;align-items:center;justify-content:center;font-family:"Montserrat",Arial,sans-serif;font-weight:800;font-size:24px;color:var(--white);letter-spacing:1px}
  .three-for-two{margin-top:2px;font-family:"Montserrat",Arial,sans-serif;font-weight:900;color:var(--pink);line-height:1;display:flex;justify-content:center;align-items:center;gap:10px}
  .three-for-two .num{font-size:118px}
  .three-for-two .for{font-size:40px;font-weight:800}
  .promo-note{margin-top:14px;font-size:14px;line-height:19px;color:#555}

  .carpet-stack{position:absolute;top:28px;left:350px;width:280px;height:340px}
  .carpet{position:absolute;border:5px solid rgba(255,255,255,.25)}
  .carpet-a{top:10px;left:70px;width:180px;height:250px;transform:rotate(4deg);background:linear-gradient(135deg,#2a4d8f,#3c2f7a 50%,#1e6f8c)}
  .carpet-b{top:50px;left:20px;width:180px;height:250px;transform:rotate(-6deg);background:linear-gradient(135deg,#8c2a2a,#b5552e 50%,#6e1f3a)}
  .carpet-c{top:70px;left:90px;width:170px;height:240px;transform:rotate(10deg);background:linear-gradient(135deg,#2f6b4f,#5a7d3a 50%,#2c4a5e)}
  .free-tag{position:absolute;top:262px;left:112px;width:170px;height:40px;transform:rotate(-30deg);background:var(--pink);border:2px dashed rgba(255,255,255,.8);display:flex;align-items:center;justify-content:center;font-family:"Montserrat",Arial,sans-serif;font-weight:800;font-size:17px;color:var(--white);letter-spacing:.5px}

  .new-shop{position:absolute;top:938px;left:19px;width:648px;height:98px;background:var(--blue);color:var(--white)}
  .new-shop h2{margin-top:16px;text-align:center;white-space:nowrap;font-family:"Montserrat",Arial,sans-serif;font-weight:800;font-size:19px;line-height:24px}
  .shop-details{position:absolute;top:56px;left:0;width:100%;display:flex;justify-content:space-between;padding:0 30px;font-family:"Montserrat",Arial,sans-serif;font-weight:700;font-size:17px}
  .shop-details div{display:flex;align-items:center;gap:12px}

  .social{position:absolute;top:1096px;left:0;width:800px;display:flex;justify-content:center;gap:10px}
  .social-dot{width:32px;height:32px;border-radius:50%}
  .social-dot:nth-child(odd){background:var(--pink)}
  .social-dot:nth-child(even){background:var(--blue)}

  .footer{position:absolute;top:1136px;left:0;width:800px;text-align:center;font-size:9.5px;line-height:14px;color:var(--grey-light)}
  .footer a{color:var(--pink);text-decoration:none}
</style>
</head>
<body>
  <div class="preheader">
    <p>If this newsletter is not displayed correctly, <a href="#">click here</a> to view the online version.</p>
    <p>If you haven't already, be sure to add <a href="#">news@heirloomrugs.example</a> to your safe sender list or address book.</p>
  </div>

  <main class="newsletter">
    <header class="brand">
      <span class="brand-dot"></span>
      <span class="brand-name">Heirloom Rugs</span>
    </header>

    <section class="hero">
      <div class="hero-photo" role="img" aria-label="Photo of a cosy living room with a sofa and a large patterned carpet on the floor"></div>

      <div class="spring-ribbon">
        <svg width="250" height="56" viewBox="0 0 250 56"><polygon points="0,0 250,0 238,28 250,56 0,56 12,28" fill="var(--pink)"/></svg>
        <span>Celebrating Spring!</span>
      </div>

      <div class="discount">
        <span class="discount-rule"></span>
        <span class="discount-value">-50%</span>
        <span class="discount-rule"></span>
      </div>

      <div class="offer-bar">
        <svg width="500" height="46" viewBox="0 0 500 46">
          <polygon points="0,8 24,8 24,46 0,46 10,27" fill="var(--blue-deep)"/>
          <polygon points="500,8 476,8 476,46 500,46 490,27" fill="var(--blue-deep)"/>
          <rect x="16" y="0" width="468" height="40" fill="var(--pink)"/>
        </svg>
        <p class="offer-text">BUY ONE CARPET <span class="offer-divider"></span> GET EXTRA 50% OFF</p>
      </div>
    </section>

    <section class="promo">
      <div class="promo-copy">
        <p class="plus">PLUS</p>
        <div class="ribbon">
          <svg width="270" height="48" viewBox="0 0 270 48"><polygon points="0,0 270,0 256,24 270,48 0,48 14,24" fill="var(--blue)"/></svg>
          <span>PROMOTION</span>
        </div>
        <p class="three-for-two"><span class="num">3</span><span class="for">for</span><span class="num">2</span></p>
        <div class="ribbon">
          <svg width="270" height="48" viewBox="0 0 270 48"><polygon points="0,0 270,0 256,24 270,48 0,48 14,24" fill="var(--blue)"/></svg>
          <span>COUPON</span>
        </div>
        <p class="promo-note">Choose ANY three carpets.<br>The lowest priced carpet will be free.</p>
      </div>

      <div class="carpet-stack">
        <div class="carpet carpet-a" role="img" aria-label="Blue vintage patterned carpet"></div>
        <div class="carpet carpet-b" role="img" aria-label="Red vintage patterned carpet"></div>
        <div class="carpet carpet-c" role="img" aria-label="Green vintage patterned carpet"></div>
        <div class="free-tag">FREE CARPET</div>
      </div>
    </section>

    <section class="new-shop">
      <h2>WE HAVE OPENED A NEW SHOP IN BERLIN, GERMANY!</h2>
      <div class="shop-details">
        <div>
          <svg width="18" height="26" viewBox="0 0 18 26" aria-hidden="true"><path d="M9 0C4 0 0 4 0 9c0 7 9 17 9 17s9-10 9-17c0-5-4-9-9-9zm0 13a4 4 0 1 1 0-8 4 4 0 0 1 0 8z" fill="var(--white)"/></svg>
          <span>Musterweg 12, 10115 Berlin</span>
        </div>
        <div>
          <svg width="24" height="24" viewBox="0 0 24 24" aria-hidden="true"><rect width="24" height="24" rx="3" fill="var(--white)"/><path d="M7 5l3 0 1 4-2 1.5c1 2 2.5 3.5 4.5 4.5L15 13l4 1v3c0 1-1 2-2 2C11 19 5 13 5 7c0-1 1-2 2-2z" fill="var(--blue)"/></svg>
          <span>+49 30 5550 1947</span>
        </div>
      </div>
    </section>
  </main>

  <nav class="social" aria-label="Social channels">
    <span class="social-dot"></span>
    <span class="social-dot"></span>
    <span class="social-dot"></span>
    <span class="social-dot"></span>
    <span class="social-dot"></span>
  </nav>

  <footer class="footer">
    <p>If you don't want to receive this Newsletter any more, please <a href="#">unsubscribe</a>.</p>
    <p><a href="#">Privacy policy</a> | <a href="#">Terms &amp; Conditions</a> | <a href="#">Contact Us</a></p>
    <p>Copyright © 2016 HEIRLOOM RUGS</p>
    <p>14 Harbour Lane and Market Street, Sample City 10001, 555-0199</p>
  </footer>
</body>
</html>
```